Graphic Design Project

ok I have the artwork for my presentation folder, and I have the text to put on the folder, I need you to apply text to the folder and the single sheets, so inside the artwork is pictures to use, text to use. thank you so much ask me as many questions as you need
Updates

my girl forgot to upload the mock ups of the presentation folder and single sheets, my apologies please check updated files

Hey Guys this is a eazy project the artwork is done, the text is done, the pictures are done!, all you have to do is assemble the project, I even have mock up pictures of how project looks finished, I have made the money good so that you would not pass on this project because it is not that creative of a job!

Target Market(s)

Dr's and patients

Industry/Entity Type

Graphic Design

Requirements
Must have
• use the single sheet artwork to make as many single sheets as you need to use all of the text supplied
Should not have
• do not make this, so professional looking that it does not appeal to the patients

```html
<!DOCTYPE html>
<html lang="en">
<head>
<meta charset="utf-8">
<title>Bayview Counseling – Presentation Folder</title>
<link rel="stylesheet" href="https://fonts.googleapis.com/css2?family=Gelasio:wght@400&display=swap">
<style>
  :root {
    --brown: #744a28;
    --text-brown: #6b4529;
    --panel-grey: #d2d3d5;
    --panel-beige: #d9d0bf;
    --paper: #ffffff;
    --white: #ffffff;
  }
  html, body {
    margin: 0;
    padding: 0;
    overflow: hidden;
    background: var(--paper);
  }
  .folder {
    position: relative;
    width: 1200px;
    height: 803px;
    overflow: hidden;
    background: var(--paper);
    font-family: "Gelasio", Georgia, serif;
  }
  .folder-shapes {
    position: absolute;
    inset: 0;
  }
  .shape-brown { fill: var(--brown); }
  .shape-grey { fill: var(--panel-grey); }
  .shape-beige { fill: var(--panel-beige); }

  .message {
    position: absolute;
    left: 574px;
    top: 24px;
    width: 572px;
    color: var(--text-brown);
    font-size: 12.2px;
    line-height: 14.8px;
  }
  .message p {
    margin: 0 0 14.8px;
  }
  .mission {
    position: absolute;
    left: 39px;
    top: 621px;
    width: 270px;
    color: var(--white);
    font-size: 11.6px;
    line-height: 14.8px;
    margin: 0;
  }
  .brand {
    position: absolute;
    left: 384px;
    top: 662px;
    color: var(--text-brown);
  }
  .brand-name {
    display: flex;
    align-items: center;
    gap: 8px;
    font-size: 24px;
    line-height: 1;
  }
  .brand-dot {
    width: 14px;
    height: 14px;
    border-radius: 50%;
    background: var(--brown);
  }
  .brand-tagline {
    margin-top: 6px;
    font-size: 11px;
    color: #3a2a1e;
    letter-spacing: 0.2px;
  }
</style>
</head>
<body>
<main class="folder">
  <svg class="folder-shapes" width="1200" height="803" viewBox="0 0 1200 803" aria-hidden="false">
    <defs>
      <linearGradient id="portrait-smoker" x1="0" y1="0" x2="1" y2="1">
        <stop offset="0" stop-color="#a9b98a"/>
        <stop offset="0.45" stop-color="#d9c3b3"/>
        <stop offset="1" stop-color="#3b3a34"/>
      </linearGradient>
      <linearGradient id="portrait-friends" x1="0" y1="0" x2="1" y2="1">
        <stop offset="0" stop-color="#4d6f98"/>
        <stop offset="0.5" stop-color="#b88f72"/>
        <stop offset="1" stop-color="#9fb3c8"/>
      </linearGradient>
    </defs>

    <path class="shape-brown" d="M20 5 H518 Q530 5 528 18 L512 98 Q508 116 488 114 L40 20 Q20 16 20 5 Z"/>

    <path class="shape-grey" d="M527 0 L1200 38 V400 L1168 520 Q1160 548 1132 542 L478 394 Q448 386 456 356 L532 12 Z"/>

    <path fill="url(#portrait-smoker)" role="img" aria-label="Photo: smiling older woman with white hair holding a cigarette"
          d="M0 62 Q10 58 40 62 L448 168 Q472 176 466 200 L380 576 Q374 596 350 590 L0 506 Z"/>

    <path class="shape-brown" d="M0 532 L305 612 Q342 622 340 652 L330 803 H0 Z"/>

    <path class="shape-beige" d="M438 404 L601 444 V803 H540 L372 762 Q348 754 354 730 L420 420 Q426 400 438 404 Z"/>

    <path fill="url(#portrait-friends)" role="img" aria-label="Photo: two smiling older women sitting together"
          d="M601 444 L1092 552 Q1116 558 1112 582 L1082 803 H601 Z"/>

    <path class="shape-beige" d="M1200 385 V645 Q1180 642 1176 620 L1196 400 Z"/>
    <path class="shape-grey" d="M1200 662 V803 H1120 L1140 700 Q1148 668 1180 664 Z"/>
  </svg>

  <section class="message">
    <p>Good patient education can be invaluable to both physician and patient.&nbsp; A patient who is educated about his or her health issues is far better prepared to work with their physician as a partner in managing their pain.&nbsp; Those patients are also more likely to have an internal locus - not expecting the doctor to "fix" everything, but relying on themselves as well.&nbsp; Understanding their medications equals better compliance.</p>
    <p>Educating your patients equals less opioid misuse and abuse and all of this leads to healthier and happier patients and makes treatment easier for their physicians.</p>
    <p>Bayview's dedicated and experienced counselors radiate a contagious interest in the life of our patients, within an intimate, caring environment that engenders transformative learning.</p>
    <p>We are determined to emphasize high ethical standards in all aspects of our counseling center.</p>
    <p>Bayview Counseling will always place the patient’s interest first and endeavor to earn and maintain the patient’s trust from the very beginning.</p>
    <p>We will hold our reputation and the integrity of our counseling center before the community in which we serve.</p>
    <p>From an ethical standpoint, our patients will feel that our office is a “safe and warm” place to be.</p>
    <p>At Bayview Counseling, We are committed to educating and informing your patients and making a difference in their lives and the lives of their loved ones.</p>
    <p>Education, Assessment, Prevention &amp; Screening</p>
  </section>

  <p class="mission">Bayview Counseling is dedicated to providing an unprecedented level of information, resources and educational support to your patients. We are committed to promoting a culture of transparency, documentation for doctors, meaningful interaction and active participation that will allow patients to assume a greater role in their healthcare through pro active addiction education, assessment, prevention, and screening</p>

  <div class="brand">
    <div class="brand-name"><span class="brand-dot"></span>Bayview Counseling</div>
    <div class="brand-tagline">a pro active addiction center</div>
  </div>
</main>
</body>
</html>
```